New Architectural Firm Business Cards

New Business card to compliment previous pixel forum logo (attached). Please design a business card that is simple, modern, creative....please do not use "symbols", simply the logo and associated graphics/text. The front should contain name/address/phone/email/web address (with graphics).....back should be 100% graphic design using the logo somehow. Hoping for a two color (black and yellow) design. full bleed design, no borders

Target Market(s)

Commercial Architecture Clients

Industry/Entity Type

Architecture

Contact Information for Business Card

Please design a business card that is simple, modern, creative....please do not use "symbols", simply the logo and associated graphics/text. The front should contain name/address/phone/email/web address (with graphics).....back should be 100% graphic design using the logo somehow

Font styles to use
Sans Serif

Colors
FFF300
FFF600
FEFA6F
FFFEC7
FFFEE8

Requirements
Must have
• Clean, Modern Design
Should not have
• Stock images or "icons"

```html
<!DOCTYPE html>
<html lang="en">
<head>
<meta charset="utf-8">
<title>Pixel Forum – Business Card</title>
<link href="https://fonts.googleapis.com/css2?family=Open+Sans:wght@400;700&display=swap" rel="stylesheet">
<style>
  :root {
    --stage: #2e3135;
    --card-white: #ffffff;
    --brand-yellow: #f6c500;
    --ink: #333333;
    --ink-soft: #555555;
    --mark-white: #ffffff;
  }
  * { margin: 0; padding: 0; box-sizing: border-box; }
  html, body {
    width: 1200px;
    height: 800px;
    overflow: hidden;
    background: var(--stage);
    font-family: "Open Sans", sans-serif;
  }
  .stage {
    position: relative;
    width: 1200px;
    height: 800px;
  }
  .card {
    position: absolute;
    top: 246px;
    width: 540px;
    height: 308px;
  }
  .card--front {
    left: 40px;
    background: var(--card-white);
    color: var(--ink);
  }
  .card--back {
    left: 620px;
    background: var(--brand-yellow);
    display: flex;
    align-items: center;
    justify-content: center;
  }
  .person {
    position: absolute;
    left: 28px;
    top: 30px;
  }
  .person__name {
    font-size: 22px;
    font-weight: 400;
    line-height: 1.2;
  }
  .person__title {
    font-size: 16px;
    color: var(--ink-soft);
    line-height: 1.3;
  }
  .brand {
    position: absolute;
    right: 30px;
    top: 28px;
    display: flex;
    align-items: center;
    gap: 10px;
  }
  .brand__dot {
    width: 22px;
    height: 22px;
    border-radius: 50%;
    background: var(--brand-yellow);
  }
  .brand__name {
    font-size: 26px;
    font-weight: 700;
    color: var(--brand-yellow);
    line-height: 1;
  }
  .contact {
    position: absolute;
    right: 30px;
    top: 140px;
    display: grid;
    grid-template-columns: auto auto;
    column-gap: 22px;
    row-gap: 4px;
    font-size: 14px;
    color: var(--ink-soft);
  }
  .contact__label { text-align: left; }
  .contact__value { text-align: right; }
  .address {
    position: absolute;
    left: 28px;
    bottom: 26px;
    font-size: 14px;
    line-height: 1.45;
    color: var(--ink-soft);
    font-style: normal;
  }
  .back-mark {
    display: flex;
    align-items: center;
    gap: 16px;
  }
  .back-mark__dot {
    width: 44px;
    height: 44px;
    border-radius: 50%;
    background: var(--mark-white);
  }
  .back-mark__name {
    font-size: 52px;
    font-weight: 700;
    color: var(--mark-white);
    line-height: 1;
  }
</style>
</head>
<body>
  <main class="stage">
    <section class="card card--front" aria-label="Business card front">
      <div class="person">
        <p class="person__name">Jonah Pellworth</p>
        <p class="person__title">Co-Funder</p>
      </div>

      <div class="brand">
        <span class="brand__dot"></span>
        <span class="brand__name">Pixel Forum</span>
      </div>

      <div class="contact">
        <span class="contact__label">M</span>
        <span class="contact__value">555 0142 7788</span>
        <span class="contact__label">E</span>
        <span class="contact__value">info@pixelforum.com</span>
        <span class="contact__label">W</span>
        <span class="contact__value">www.pixelforum.com</span>
      </div>

      <address class="address">
        88 Harbor Lane<br>
        Fairview CA 5510<br>
        United States
      </address>
    </section>

    <section class="card card--back" aria-label="Business card back">
      <div class="back-mark">
        <span class="back-mark__dot"></span>
        <span class="back-mark__name">Pixel Forum</span>
      </div>
    </section>
  </main>
</body>
</html>
```